Project Planning & Communication Process

Need a PowerPoint slide that illustrates our project planning and communication cycle. Our company has key meetings, and key communication vehicles (like emails and follow up tools) that we use to ensure our frontline staff are prepared to execute the new project successfully. This document needs to call out how the different components, like the meetings and emails, work together (like a flow chart), so someone who needs to use this process will understand what they should do. The slide needs to be simple yet comprehensive enough to guide someone through the details. I don't want it overwhelming. The primary focus is the process, not the details.

Use the color pallette included within the slide (shades of blue and gray, and black). This is for an insurance company (www.harborquill.com). Use this as a reference for the look and feel.

I have attached a sample slide of the flow chart process.

Click here if you cannot access the file. https://www.filecrate.example/s/q8wz2mbt7ypnc4r/Communcation_Methods_V1.pptx

If you are not able to see the uploaded slide.  Please send me your email address and I will send the slide to you directly. 

ISince I'm not able to upload the reference ppt file, 've uploaded the slide at FileCrate.  Please click here to access.
https://www.filecrate.example/s/q8wz2mbt7ypnc4r/Communcation_Methods_V1.pptx

Reason: extending one more day for designers to make last minute updates.

Target Market(s)

Vice Presidents and project managers/business partners within the organization.

Industry/Entity Type

Communication

Font styles to use
Sans Serif

Colors
3176b5

Requirements
Must have
• 1 page, color pallette assigned, be simple yet comprehensive. the focus needs to be on the process, not on the details.
Nice to have
• Doesn't have to follow the example I provided. Please feel free to approach from different ways.

```html
<!DOCTYPE html>
<html lang="en">
<head>
<meta charset="utf-8">
<title>Project Alignment &amp; Project Communication Process</title>
<link href="https://fonts.googleapis.com/css2?family=Carlito:wght@400;700&display=swap" rel="stylesheet">
<style>
:root{
  --title-grey:#a6a6a6;
  --band-light:#f2f2f2;
  --band-mid:#bfbfbf;
  --band-dark:#7f7f7f;
  --step-grey:#bfbfbf;
  --meeting-blue:#4f81bd;
  --meeting-blue-deep:#3176b5;
  --tool-navy:#10243e;
  --arrow:#b4c7e7;
  --note-light:#f2f2f2;
  --note-mid:#bfbfbf;
  --ink:#000;
  --white:#fff;
}
*{box-sizing:border-box;margin:0;padding:0}
html,body{width:1200px;height:900px;overflow:hidden;background:var(--white)}
body{font-family:"Carlito","Calibri",Arial,sans-serif;color:var(--ink)}
.slide{position:relative;width:1200px;height:900px}
.abs{position:absolute}
.title-bar{left:0;top:0;width:1200px;height:69px;background:linear-gradient(#b2b2b2,var(--title-grey));color:var(--white);font-size:33px;display:flex;align-items:center;justify-content:flex-end;padding-right:14px}
.phase{display:flex;align-items:center;justify-content:center;text-align:center;font-size:25px}
.phase-plan{left:20px;top:80px;width:720px;height:48px;background:var(--band-light)}
.phase-prepare{left:771px;top:80px;width:308px;height:48px;background:var(--band-mid)}
.phase-follow{left:1090px;top:80px;width:108px;height:95px;background:var(--band-dark);color:var(--white);font-size:21px;line-height:1.3}
.timing{background:var(--band-light);font-size:13px;display:flex;align-items:center;justify-content:center;text-align:center;line-height:1.2}
.timing-dark{background:var(--band-mid)}
.step{top:200px;height:225px;border-radius:6px;color:var(--white);display:flex;flex-direction:column;align-items:center;justify-content:center;text-align:center;font-size:15px;line-height:1.2;padding:0 4px}
.step-grey{background:var(--step-grey)}
.step-meeting{background:var(--meeting-blue)}
.step-tool{background:var(--tool-navy)}
.step b{font-weight:700}
.step .detail{font-size:10px;font-weight:700;margin-top:14px;line-height:1.25}
.step .sub{margin-top:16px}
.arrow{top:301px;width:18px;height:22px}
.note{font-size:13.5px;line-height:1.33;padding:6px 10px 6px 12px}
.note-light{background:var(--note-light)}
.note-mid{background:var(--note-mid)}
.note b{display:block}
.purpose{top:432px;height:122px}
.overview{top:578px;height:251px}
.legend{left:1016px;width:163px;color:var(--white);display:flex;align-items:center;justify-content:center;border-radius:6px}
.legend-meetings{top:790px;height:31px;background:var(--meeting-blue);font-size:24px;border-radius:3px}
.legend-tools{top:830px;height:49px;background:var(--tool-navy);font-size:20px}
</style>
</head>
<body>
<main class="slide">
  <header class="abs title-bar">Project Alignment &amp; Project Communication Process</header>

  <div class="abs phase phase-plan">Planning &amp; Design Phase</div>
  <div class="abs phase phase-prepare">Prepare Phase</div>
  <div class="abs phase phase-follow">Follow<br>Up &amp;<br>Evaluate</div>

  <div class="abs timing" style="left:125px;top:156px;width:125px;height:30px">3 + Months out</div>
  <div class="abs timing" style="left:520px;top:156px;width:110px;height:28px">2+ months out</div>
  <div class="abs timing timing-dark" style="left:771px;top:150px;width:83px;height:39px">1 month<br>out</div>
  <div class="abs timing timing-dark" style="left:893px;top:150px;width:62px;height:39px">1 Week<br>out</div>

  <div class="abs step step-grey" style="left:20px;width:78px">New Project Identified</div>
  <div class="abs step step-meeting" style="left:134px;width:100px">Governance Meeting</div>
  <div class="abs step step-grey" style="left:270px;width:79px">Separate Project Meetings as needed</div>
  <div class="abs step step-meeting" style="left:385px;width:119px"><b>Governance Meeting</b></div>
  <div class="abs step step-meeting" style="left:540px;width:76px"><b>Weekly Center Leader Meeting</b></div>
  <div class="abs step step-meeting" style="left:655px;width:78px;justify-content:flex-start;padding-top:28px"><b>Field Advisory Panel</b>
    <span class="detail">Purpose:<br>Collect Feedback</span>
    <span class="detail">When: As needed</span></div>
  <div class="abs step step-meeting" style="left:771px;width:78px;background:var(--meeting-blue-deep);justify-content:flex-start;padding-top:6px"><b style="font-size:13px">Weekly Center Leader Meeting</b>
    <span class="detail">Purpose:<br>Center Planning and Specific execution details</span>
    <span class="detail">When: 1 month out</span></div>
  <div class="abs step step-tool" style="left:885px;width:78px">Monday Memo<span class="sub">1 week out</span></div>
  <div class="abs step step-tool" style="left:999px;width:79px;justify-content:flex-start;padding-top:54px"><b style="font-size:14px">Daily Digest</b>
    <span class="detail" style="font-weight:400">Just in Time Notice/Follow up for execution</span></div>
  <div class="abs step step-tool" style="left:1114px;width:77px">Follow Up Guide<span class="sub">Post Launch</span></div>

  <svg class="abs arrow" style="left:107px" viewBox="0 0 18 22" aria-hidden="true"><path d="M0 6h9V0l9 11-9 11v-6H0z" fill="var(--arrow)"/></svg>
  <svg class="abs arrow" style="left:244px" viewBox="0 0 18 22" aria-hidden="true"><path d="M0 6h9V0l9 11-9 11v-6H0z" fill="var(--arrow)"/></svg>
  <svg class="abs arrow" style="left:359px" viewBox="0 0 18 22" aria-hidden="true"><path d="M0 6h9V0l9 11-9 11v-6H0z" fill="var(--arrow)"/></svg>
  <svg class="abs arrow" style="left:514px" viewBox="0 0 18 22" aria-hidden="true"><path d="M0 6h9V0l9 11-9 11v-6H0z" fill="var(--arrow)"/></svg>
  <svg class="abs arrow" style="left:627px" viewBox="0 0 18 22" aria-hidden="true"><path d="M0 6h9V0l9 11-9 11v-6H0z" fill="var(--arrow)"/></svg>
  <svg class="abs arrow" style="left:744px" viewBox="0 0 18 22" aria-hidden="true"><path d="M0 6h9V0l9 11-9 11v-6H0z" fill="var(--arrow)"/></svg>
  <svg class="abs arrow" style="left:858px" viewBox="0 0 18 22" aria-hidden="true"><path d="M0 6h9V0l9 11-9 11v-6H0z" fill="var(--arrow)"/></svg>
  <svg class="abs arrow" style="left:972px" viewBox="0 0 18 22" aria-hidden="true"><path d="M0 6h9V0l9 11-9 11v-6H0z" fill="var(--arrow)"/></svg>
  <svg class="abs arrow" style="left:1087px" viewBox="0 0 18 22" aria-hidden="true"><path d="M0 6h9V0l9 11-9 11v-6H0z" fill="var(--arrow)"/></svg>

  <div class="abs note note-light purpose" style="left:125px;width:111px"><b>Purpose:</b>Go/No Go Decision</div>
  <div class="abs note note-light purpose" style="left:395px;width:109px"><b>Purpose:</b>Report out on Milestone status and Key Decision Points</div>
  <div class="abs note note-light purpose" style="left:520px;width:110px"><b>Purpose:</b>Introduce Project &amp; gather Center Leader Feedback</div>
  <div class="abs note note-light purpose" style="left:640px;width:110px"><b>Purpose:</b>Collect Center Staff Feedback</div>
  <div class="abs note note-mid purpose" style="left:760px;width:109px"><b>Purpose:</b>Provide Center Leaders with Implementation Details</div>

  <div class="abs note note-light overview" style="left:125px;width:111px"><b>Overview:</b>Project Owner presents one pager to Sr Leadership. Based on Business Value, and Capacity a Go/No Go Decision is made.</div>
  <div class="abs note note-light overview" style="left:395px;width:109px"><b>Overview:</b>Project Owner presents milestones and feedback/approvals during key decision points.</div>
  <div class="abs note note-light overview" style="left:520px;width:110px"><b>Overview:</b>Project Owner provides overview of project, collects center leader feedback.</div>
  <div class="abs note note-light overview" style="left:640px;width:110px"><b>Overview:</b>Project Owner presents project and collect Center Staff Feedback</div>
  <div class="abs note note-mid overview" style="left:760px;width:109px"><b>Overview:</b>Project Owner presents project and implementation details to ensure Center Leaders are prepared.</div>

  <div class="abs legend legend-meetings">Meetings</div>
  <div class="abs legend legend-tools">Emails/Tools</div>
</main>
</body>
</html>
```